Powerpoint template for Trivia Company

Revamp of our current powerpoint template to make it more professional and fun for the players. Something worthy of a trivia company. Please see logo attached for potential colour - but also open to other ideas.

NO BRANDING REQUIRED (IE: No mention of our company or logo on the template please)

Target Market(s)

Bars/restaurants

Colors
3176b5
00a990

```html
<!DOCTYPE html>
<html lang="en">
<head>
<meta charset="utf-8">
<title>Trivia Night Slides – Final Round</title>
<link rel="stylesheet" href="https://fonts.googleapis.com/css2?family=Montserrat:wght@400;500;700;800;900&display=swap">
<style>
  :root {
    --ink: #000000;
    --white: #ffffff;
    --teal: #00a990;
    --blue: #3176b5;
    --sky: #1ba6d8;
    --green: #6cb33f;
    --yellow: #ffd400;
    --orange: #f58a1f;
    --red: #e8352b;
    --purple: #8a2f97;
    --flame: #f04e23;
    --sun: #ffe600;
    --page-top: #ffffff;
    --page-bottom: #9c9c9c;
  }
  * { box-sizing: border-box; margin: 0; padding: 0; }
  html, body { width: 960px; height: 1200px; overflow: hidden; }
  body {
    background: linear-gradient(180deg, var(--page-top) 0%, #e6e6e6 25%, #b9b9b9 55%, var(--page-bottom) 100%);
    font-family: "Montserrat", sans-serif;
    position: relative;
  }
  .slide {
    position: absolute;
    width: 429px;
    height: 252px;
    background: radial-gradient(circle at 50% 50%, #2a1d16 0%, #120c09 35%, var(--ink) 75%);
    color: var(--white);
    text-align: center;
    overflow: hidden;
  }
  .slide::after {
    content: "";
    position: absolute;
    left: 0; right: 0; bottom: 0;
    height: 3px;
    background: linear-gradient(90deg,
      var(--red) 0 17%, var(--blue) 17% 34%, var(--sky) 34% 51%,
      var(--green) 51% 67%, var(--yellow) 67% 84%, var(--orange) 84% 100%);
  }
  .col-left { left: 31px; }
  .col-right { left: 502px; width: 427px; }
  .row-1 { top: 31px; }
  .row-2 { top: 317px; }
  .row-3 { top: 600px; }
  .row-4 { top: 893px; }

  .heading-teal { color: var(--teal); font-weight: 800; text-transform: uppercase; letter-spacing: 0.2px; }
  .strong { font-weight: 800; }

  /* Get ready */
  .get-ready { padding-top: 33px; }
  .get-ready__title { font-size: 33px; font-weight: 900; line-height: 1; }
  .get-ready__body { font-size: 19px; font-weight: 700; line-height: 25.5px; margin-top: 12px; padding: 0 30px; }
  .get-ready__category { font-size: 25.5px; line-height: 27px; margin-top: 16px; }

  /* Final question */
  .final-q { padding-top: 55px; }
  .final-q__title { font-size: 25px; line-height: 1; }
  .final-q__body { font-size: 21px; font-weight: 500; line-height: 25.5px; margin-top: 17px; padding: 0 40px; }

  /* Bring answers */
  .handin { display: flex; align-items: center; justify-content: center; }
  .handin__text { font-size: 25.5px; font-weight: 800; line-height: 30.5px; }
  .handin__text .accent { color: var(--teal); }

  /* Film answers */
  .answers__title { font-size: 20px; line-height: 1; margin-top: 27px; }
  .film-list {
    position: absolute; left: 62px; top: 69px;
    list-style: none; text-align: left;
    font-size: 8.6px; font-weight: 700; line-height: 14px;
  }
  .posters { position: absolute; left: 139px; top: 134px; display: flex; gap: 6px; }
  .poster { position: relative; width: 58px; height: 88px; border: 2px solid var(--white); }
  .poster__art { width: 100%; height: 100%; }
  .poster--1 .poster__art { background: linear-gradient(90deg, #d9d9d9, #6b6b6b 50%, #111 52%, #cfcfcf); }
  .poster--2 .poster__art { background: linear-gradient(180deg, #3b2a1c, #7a4e2a 55%, #1a120c); }
  .poster--3 .poster__art { background: linear-gradient(180deg, #d9c7a6, #a37c50 55%, #4a3423); }
  .poster--4 .poster__art { background: linear-gradient(180deg, #1e3f74, #4b78b3 55%, #0f2246); }
  .poster__badge {
    position: absolute; left: 50%; top: -12px; transform: translateX(-50%);
    width: 21px; height: 21px; border-radius: 50%;
    background: var(--teal); color: var(--white);
    font-size: 13px; font-weight: 800; line-height: 21px; text-align: center;
  }

  /* Tie breaker */
  .tie { padding-top: 56px; }
  .tie__title { font-size: 26.5px; line-height: 1; }
  .tie__body { font-size: 22px; font-weight: 500; line-height: 27.5px; margin-top: 16px; padding: 0 50px; }

  /* Tie answer */
  .icon-disc {
    position: absolute; left: 50%; transform: translateX(-50%);
    border-radius: 50%; background: var(--white);
  }
  .icon-disc__art { position: absolute; inset: 22%; border-radius: 50%; }
  .tie-answer .icon-disc { top: 54px; width: 104px; height: 104px; }
  .tie-answer .icon-disc__art { background: radial-gradient(circle, #a9c6e6, #e9f0f8); }
  .tie-answer__value { position: absolute; left: 0; right: 0; top: 163px; font-size: 39px; font-weight: 900; line-height: 1; }
  .tie-answer__note { position: absolute; left: 0; right: 0; top: 207px; font-size: 20px; font-weight: 800; line-height: 1; }

  /* Winners */
  .slide--winners { background: radial-gradient(circle at 50% 35%, #fff36a 0%, var(--sun) 40%, #ffd900 100%); }
  .slide--winners .icon-disc { top: 20px; width: 119px; height: 119px; }
  .slide--winners .icon-disc__art { background: radial-gradient(circle, #c79ad0, #f4e9f6); }
  .winners__line1 { position: absolute; left: 0; right: 0; top: 150px; font-size: 38px; font-weight: 900; color: var(--purple); line-height: 1; }
  .winners__line2 { position: absolute; left: 0; right: 0; top: 190px; font-size: 38px; font-weight: 900; color: var(--flame); line-height: 1; }

  /* Farewell */
  .farewell .icon-disc { top: 19px; width: 118px; height: 118px; }
  .farewell .icon-disc__art { background: radial-gradient(circle, #8fd8cb, #e8f7f4); }
  .farewell__text { position: absolute; left: 0; right: 0; top: 141px; font-size: 27px; font-weight: 800; line-height: 30.5px; }
  .farewell__text .accent { color: var(--teal); }
</style>
</head>
<body>

<section class="slide col-left row-1 get-ready">
  <h1 class="get-ready__title">Get Ready</h1>
  <p class="get-ready__body">for the Final Trivia Round which is worth up to 20 points.&nbsp; How much are you going to wager?</p>
  <p class="get-ready__category heading-teal">Category:&nbsp; Movie Star Collaborations</p>
</section>

<section class="slide col-right row-1 final-q">
  <h2 class="final-q__title heading-teal">Final Question</h2>
  <p class="final-q__body">Name 3 of the 4 films that <span class="strong">Marla Quinn</span> and <span class="strong">Dorian Vale</span> have starred in together</p>
</section>

<section class="slide col-left row-2 handin">
  <p class="handin__text">Once you’ve<br>completed your answers,<br>please bring them to the<br><span class="accent">Quizmaster</span></p>
</section>

<section class="slide col-right row-2 answers">
  <h2 class="answers__title heading-teal">Answers</h2>
  <ol class="film-list">
    <li>1. Bright Side Story (2012)</li>
    <li>2. Velvet Con (2013)</li>
    <li>3. Timberline (2014)</li>
    <li>4. Spark (2015)</li>
  </ol>
  <div class="posters">
    <div class="poster poster--1"><div class="poster__art" role="img" aria-label="Film poster for Bright Side Story"></div><span class="poster__badge">1</span></div>
    <div class="poster poster--2"><div class="poster__art" role="img" aria-label="Film poster for Velvet Con"></div><span class="poster__badge">2</span></div>
    <div class="poster poster--3"><div class="poster__art" role="img" aria-label="Film poster for Timberline"></div><span class="poster__badge">3</span></div>
    <div class="poster poster--4"><div class="poster__art" role="img" aria-label="Film poster for Spark"></div><span class="poster__badge">4</span></div>
  </div>
</section>

<section class="slide col-left row-3 tie">
  <h2 class="tie__title heading-teal">Tie Breaker Question</h2>
  <p class="tie__body">In hours, what is the average <span class="strong">gestation period of a fox?</span></p>
</section>

<section class="slide col-right row-3 tie-answer">
  <h2 class="answers__title heading-teal">Answers</h2>
  <div class="icon-disc"><div class="icon-disc__art" role="img" aria-label="Blue line icon of a sitting fox"></div></div>
  <p class="tie-answer__value">1248 hours</p>
  <p class="tie-answer__note">(52 day average)</p>
</section>

<section class="slide slide--winners col-left row-4">
  <div class="icon-disc"><div class="icon-disc__art" role="img" aria-label="Purple line icon of a trophy with burst lines"></div></div>
  <p class="winners__line1">Congratulations</p>
  <p class="winners__line2">to the winners!</p>
</section>

<section class="slide col-right row-4 farewell">
  <div class="icon-disc"><div class="icon-disc__art" role="img" aria-label="Teal line icon of clapping hands"></div></div>
  <p class="farewell__text"><span class="accent">Hope Everyone had a<br>great time,</span> see you all<br>next time!</p>
</section>

</body>
</html>
```